Marijuana Lifestyle Multi-Shop Brand Website

We need a website that provides an online retail shop for our products, along with the additional functionality:

Main Page: Slider with great photography (we are still looking for a professional photographer to take photos for us.

Shop Tab: E-commerce site.
- Main Categories:
- Accessories
- Bubblers
- Dry Pieces
- Scientific Glass
- Water Pipes
- Custom Shop
- University Store

Stores/Resellers: This is a store look-up, so people can enter their zipcode and find our resellers and partners.

Brand Partners: Just a basic filter and page so that we can highlight our partners and why we've selected them.

Contact Us: Basic Form
- Career Page: Basic Page

About Us: Basic Page

Blog:

Search Bar:

Essentially, we want a near exact copy of this website, but with our brand, logo and content. https://corkwillowbins.com/

This site is really really simple, but we like simple.

Our reserved domain address is: www.runbaketend.com

About Us:
We are multi-shop for marijuana-related accessories. We sell quality glass pipes, vaporizers, amazing storage options, dime bags, custom t-shirts and other stuff.

We have a network of resellers that allow us to put in micro-installations into gift shops, convenience stores, tobacco stores, etc. and we are trying to change the overall perception that buying these items should be mainstream and as transparent as going to the Fen or the Walnut Shop.

I've attached a logo that should give you an idea of our color scheme. We don't have our photography yet for the slider
Updates

As an FYI, for the e-commerce part of my website, I already have a license for WP SwiftTill.

Industry/Entity Type

Shop

```html
<!DOCTYPE html>
<html lang="en">
<head>
<meta charset="utf-8">
<title>ferntide — Home</title>
<link rel="stylesheet" href="https://fonts.googleapis.com/css2?family=Noticia+Text:wght@400;700&display=swap">
<style>
  :root {
    --cream: #f5f8e3;
    --olive-dark: #394707;
    --olive-tab: #3d4c0c;
    --nav-text: #3f4a1c;
    --footer-text: #bcc792;
    --leaf-deep: #2f6a12;
    --leaf-mid: #4f9a1c;
    --leaf-light: #9cc83a;
    --arrow-fill: rgba(110, 120, 95, 0.85);
    --arrow-ring: rgba(235, 240, 215, 0.9);
    --dot: rgba(220, 228, 205, 0.75);
  }
  * { margin: 0; padding: 0; box-sizing: border-box; }
  html, body { width: 1200px; height: 845px; overflow: hidden; }
  body {
    position: relative;
    background: var(--cream);
    font-family: "Noticia Text", Georgia, serif;
  }
  .site-header {
    position: absolute; top: 0; left: 0; width: 1200px; height: 234px;
    background: var(--cream);
  }
  .brand {
    position: absolute; top: 86px; left: 0; width: 1200px;
    display: flex; justify-content: center; align-items: center; gap: 12px;
  }
  .brand-dot {
    width: 26px; height: 26px; border-radius: 50%;
    background: var(--olive-dark);
  }
  .brand-name {
    font-size: 38px; font-weight: 700; color: var(--olive-dark);
    letter-spacing: 1px;
  }
  .main-nav {
    position: absolute; top: 199px; left: 261px; height: 35px;
    display: flex; align-items: center;
  }
  .main-nav a {
    display: block; height: 35px; line-height: 28px;
    padding: 0 13px; margin-right: 9px;
    font-size: 13px; color: var(--nav-text); text-decoration: none;
    letter-spacing: 0.5px;
  }
  .main-nav a.is-current {
    background: var(--olive-tab); color: var(--cream);
    border-radius: 4px 4px 0 0;
  }
  .main-nav .search-icon { margin-left: 4px; margin-top: -6px; }
  .hero-slider {
    position: absolute; top: 234px; left: 0; width: 1200px; height: 556px;
    box-shadow: inset 0 3px 4px rgba(0,0,0,0.35);
  }
  .hero-image {
    position: absolute; inset: 0;
    background:
      radial-gradient(circle at 50% 48%, #c8d75a 0, #7fae2a 8%, var(--leaf-mid) 22%, var(--leaf-deep) 42%, transparent 62%),
      linear-gradient(120deg, #3f7d14 0%, #6aa824 30%, #8fbf33 60%, #4b8a18 100%);
  }
  .slider-arrow {
    position: absolute; top: 243px; width: 71px; height: 71px; border-radius: 50%;
    background: var(--arrow-fill); border: 5px solid var(--arrow-ring);
  }
  .slider-arrow svg { display: block; margin: 14px auto 0; }
  .slider-arrow.prev { left: 72px; }
  .slider-arrow.next { left: 1058px; }
  .slider-dots {
    position: absolute; top: 512px; left: 539px; display: flex; gap: 10px;
  }
  .slider-dots span {
    width: 16px; height: 16px; border-radius: 50%; background: var(--dot);
  }
  .slider-dots span.is-active { background: #fff; border: 3px solid #556b22; }
  .site-footer {
    position: absolute; top: 790px; left: 0; width: 1200px; height: 55px;
    background: var(--olive-dark);
  }
  .copyright {
    position: absolute; left: 243px; top: 22px;
    font-size: 9px; color: var(--footer-text); letter-spacing: 0.5px;
  }
  .social-links {
    position: absolute; left: 792px; top: 20px; display: flex; gap: 16px;
  }
  .social-links span {
    width: 14px; height: 14px; border-radius: 50%; background: var(--footer-text);
  }
</style>
</head>
<body>
  <header class="site-header">
    <div class="brand">
      <span class="brand-dot"></span>
      <span class="brand-name">ferntide</span>
    </div>
    <nav class="main-nav">
      <a href="#" class="is-current">Home</a>
      <a href="#">Shop</a>
      <a href="#">Resellers</a>
      <a href="#">Brand Partners</a>
      <a href="#">Contact Us</a>
      <a href="#">About Us</a>
      <a href="#">Blog</a>
      <svg class="search-icon" width="11" height="11" viewBox="0 0 11 11" aria-label="Search">
        <circle cx="4.5" cy="4.5" r="3.3" fill="none" stroke="#3f4a1c" stroke-width="1.5"/>
        <line x1="7" y1="7" x2="10" y2="10" stroke="#3f4a1c" stroke-width="1.8"/>
      </svg>
    </nav>
  </header>

  <section class="hero-slider">
    <div class="hero-image" role="img" aria-label="Close-up photograph of a green flowering plant bud"></div>
    <a href="#" class="slider-arrow prev" aria-label="Previous slide">
      <svg width="32" height="32" viewBox="0 0 32 32"><polyline points="20,4 8,16 20,28" fill="none" stroke="#fff" stroke-width="3"/></svg>
    </a>
    <a href="#" class="slider-arrow next" aria-label="Next slide">
      <svg width="32" height="32" viewBox="0 0 32 32"><polyline points="12,4 24,16 12,28" fill="none" stroke="#fff" stroke-width="3"/></svg>
    </a>
    <div class="slider-dots">
      <span></span><span></span><span class="is-active"></span><span></span><span></span>
    </div>
  </section>

  <footer class="site-footer">
    <p class="copyright">ferntide Copyright &nbsp;© 2014. All Rights Reserved.</p>
    <div class="social-links" aria-label="Social links">
      <span></span><span></span><span></span><span></span><span></span>
    </div>
  </footer>
</body>
</html>
```